Design my dad a new business card because his current one sucks!

I need a business card designed for my fathers home maintenance business. His customers are individuals (single moms, old people etc.) as well as the occasional business. As such it needs to be accessible to both target audiences.

The front of the card should be dark grey on yellow with the logo and contain the following information:
- Warren Dobrinski
- 0487 362 914
- info@harbourlinehandyworks.com.au
- 0487 362 914

- ABN: 87 214 630 592
- 'Fully Insured'

The reverse should be yellow on dark grey and will have the web address:
- harbourlinehandyworks.com.au

And a few key services he offers:
GENERAL REPAIRS
PAINTING/TILING/
PAVING &CONCRETING
PRESSURE WASHING
ON-SITE WELDING
DECKING ADDITIONS & REPAIRS
FENCING
FULL BOND CLEANING

This will be first time the logo has been printed so you will need to come up with the best CMYK approximation of the RGB colours to make sure it is a close as possible.

```html
<!DOCTYPE html>
<html lang="en">
<head>
<meta charset="utf-8">
<title>Harbourline Handyworks – Business Card</title>
<link rel="stylesheet" href="https://fonts.googleapis.com/css2?family=Open+Sans:wght@400;600;700;800&display=swap">
<style>
  :root {
    --canvas: #e9e9e7;
    --yellow-light: #ffe600;
    --yellow: #fcd20a;
    --yellow-deep: #f5b800;
    --charcoal: #2b2b2b;
    --ink-soft: #3d3d3d;
    --grey-light: #7a7876;
    --grey: #666462;
    --grey-dark: #565452;
    --accent: #f2e21c;
    --web-text: #f1f1f1;
    --watermark: rgba(40, 40, 40, 0.28);
  }
  * { box-sizing: border-box; margin: 0; padding: 0; }
  html, body {
    width: 1200px; height: 873px; overflow: hidden;
    background: var(--canvas);
    font-family: "Open Sans", Arial, sans-serif;
  }
  .stage {
    position: relative; width: 1200px; height: 873px;
    display: flex; align-items: center; justify-content: center; gap: 60px;
  }
  .card {
    position: relative; width: 520px; height: 318px;
    border-radius: 4px; overflow: hidden;
    box-shadow: 0 10px 24px rgba(0,0,0,0.18);
  }

  /* Front */
  .card--front {
    background: radial-gradient(ellipse at 55% 45%, var(--yellow-light) 0%, var(--yellow) 55%, var(--yellow-deep) 100%);
    color: var(--ink-soft);
  }
  .holder-name {
    position: absolute; left: 30px; top: 26px;
    font-size: 21px; font-weight: 700; color: var(--ink-soft);
  }
  .contact-list { position: absolute; left: 30px; top: 70px; list-style: none; }
  .contact-list li {
    display: flex; align-items: center; gap: 12px;
    font-size: 14px; margin-bottom: 10px; color: var(--ink-soft);
  }
  .contact-list svg { width: 18px; height: 18px; flex: none; }
  .brand {
    position: absolute; left: 100px; top: 138px; width: 380px;
    display: flex; align-items: center; gap: 12px;
  }
  .brand__dot {
    width: 30px; height: 30px; border-radius: 50%;
    background: var(--charcoal); flex: none;
  }
  .brand__name {
    font-size: 33px; font-weight: 800; line-height: 1;
    color: var(--charcoal); letter-spacing: -0.5px;
  }
  .insured {
    position: absolute; right: 44px; top: 184px;
    font-size: 12px; color: var(--ink-soft);
  }
  .front-web {
    position: absolute; left: 30px; bottom: 24px; font-size: 13px;
  }
  .abn {
    position: absolute; right: 30px; bottom: 24px; font-size: 13px;
  }

  /* Back */
  .card--back {
    background: radial-gradient(ellipse at 60% 35%, var(--grey-light) 0%, var(--grey) 55%, var(--grey-dark) 100%);
  }
  .back-watermark {
    position: absolute; left: 150px; top: 118px;
    font-size: 40px; font-weight: 800; color: var(--watermark);
    letter-spacing: -0.5px;
  }
  .service {
    position: absolute; font-size: 13px; font-weight: 600;
    color: var(--accent); text-transform: uppercase; white-space: nowrap;
  }
  .back-web {
    position: absolute; left: 30px; bottom: 24px;
    display: flex; align-items: center; gap: 6px;
    font-size: 14px; color: var(--web-text);
  }
  .back-web svg { width: 10px; height: 14px; }
</style>
</head>
<body>
<main class="stage">

  <section class="card card--front" aria-label="Card front">
    <h1 class="holder-name">Warren Dobrinski</h1>
    <ul class="contact-list">
      <li>
        <svg viewBox="0 0 24 24" aria-hidden="true"><path fill="none" stroke="#3d3d3d" stroke-width="2" d="M6 3h3l2 5-2 1.5a11 11 0 0 0 5.5 5.5L16 13l5 2v3a2 2 0 0 1-2 2A16 16 0 0 1 4 5a2 2 0 0 1 2-2z"/></svg>
        <span>0487 362 914</span>
      </li>
      <li>
        <svg viewBox="0 0 24 24" aria-hidden="true"><rect x="3" y="6" width="18" height="12" fill="none" stroke="#3d3d3d" stroke-width="2"/><path d="M3 6l9 7 9-7" fill="none" stroke="#3d3d3d" stroke-width="2"/></svg>
        <span>info@harbourlinehandyworks.com.au</span>
      </li>
    </ul>
    <div class="brand">
      <span class="brand__dot" aria-hidden="true"></span>
      <span class="brand__name">Harbourline Handyworks</span>
    </div>
    <p class="insured">Fully Insured</p>
    <p class="front-web">harbourlinehandyworks.com.au</p>
    <p class="abn">ABN: 87 214 630 592</p>
  </section>

  <section class="card card--back" aria-label="Card back">
    <span class="back-watermark" aria-hidden="true">Harbourline</span>
    <span class="service" style="left:40px; top:30px;">General Repairs</span>
    <span class="service" style="left:40px; top:66px;">Paving &amp;Concreting</span>
    <span class="service" style="left:40px; top:102px;">On-Site Welding</span>
    <span class="service" style="left:230px; top:48px;">Full Bond Cleaning</span>
    <span class="service" style="left:230px; top:84px;">Pressure Washing</span>
    <span class="service" style="left:230px; top:120px;">Decking Additions &amp; Repairs</span>
    <span class="service" style="left:40px; top:170px;">Painting</span>
    <span class="service" style="left:230px; top:190px;">Fencing</span>
    <span class="service" style="left:410px; top:160px;">Tiling</span>
    <p class="back-web">
      <span>harbourlinehandyworks.com.au</span>
      <svg viewBox="0 0 10 14" aria-hidden="true"><path d="M1 1v11l3-3 2 4 1.5-.7-2-4H9z" fill="#f1f1f1"/></svg>
    </p>
  </section>

</main>
</body>
</html>
```